Catalogue Design Project

we are college are would like have a,

College Hand out booklet, infomation book.

this book will be used for marketing,branding, given to new students, business, all information about our college including course information, college information, eg. a university ingo book A4 in size.
we would like to have the cover pages and all internal pages designed, then the content we can do locally.

Industry/Entity Type

University

```html
<!DOCTYPE html>
<html lang="en">
<head>
<meta charset="utf-8">
<title>College Course Guide – Course Overview Spread</title>
<link href="https://fonts.googleapis.com/css2?family=Noto+Sans:wght@400;700&display=swap" rel="stylesheet">
<style>
  :root {
    --canvas-grey: #e6e7e9;
    --navy-band: #36427a;
    --sky-light: #dff5fd;
    --sky-mid: #6ccaf2;
    --sky-deep: #12a0e0;
    --card-grey: #58585a;
    --card-text: #ffffff;
    --card-body: #eeeeee;
    --photo-sky: #9fc9e6;
    --photo-mid: #7a8794;
    --photo-dark: #3e3a3a;
  }
  * { box-sizing: border-box; margin: 0; padding: 0; }
  html, body {
    width: 1200px; height: 858px; overflow: hidden;
    background: var(--canvas-grey);
    font-family: "Noto Sans", Verdana, sans-serif;
  }
  .spread {
    position: absolute; left: 19px; top: 19px;
    width: 1162px; height: 821px;
    background: radial-gradient(ellipse 62% 70% at 43% 43%, var(--sky-light) 0%, var(--sky-mid) 48%, var(--sky-deep) 100%);
    overflow: hidden;
  }
  .band { position: absolute; left: 0; width: 100%; background: var(--navy-band); }
  .band--top { top: 0; height: 40px; }
  .band--bottom { bottom: 0; height: 42px; }
  .course-card {
    position: absolute; width: 446px; height: 146px;
    background: var(--card-grey); border-radius: 19px;
    padding: 14px 30px 0 25px; color: var(--card-text);
  }
  .course-card__title { font-size: 15.5px; font-weight: 700; line-height: 20px; }
  .course-card__subtitle { font-size: 8.5px; font-weight: 700; line-height: 10px; margin-top: -1px; }
  .course-card__body {
    font-size: 7px; line-height: 9px; color: var(--card-body);
    margin-top: 11px; letter-spacing: -0.05px;
  }
  .course-card--sub .course-card__body { margin-top: 2px; }
  .course-card__code { font-size: 7px; line-height: 9px; text-align: right; margin-top: 3px; margin-right: -4px; }
  .col-left { left: 68px; }
  .col-right { left: 648px; }
  .row-1 { top: 82px; } .row-2 { top: 252px; } .row-3 { top: 422px; } .row-4 { top: 592px; }
  .student-photo {
    position: absolute; left: 581px; top: 570px; width: 581px; height: 209px;
    background:
      linear-gradient(90deg, rgba(60,180,235,0.9) 0%, rgba(60,180,235,0) 18%),
      linear-gradient(180deg, var(--photo-sky) 0%, var(--photo-mid) 55%, var(--photo-dark) 100%);
  }
</style>
</head>
<body>
<main class="spread">
  <div class="band band--top"></div>

  <section class="course-card col-left row-1">
    <h2 class="course-card__title">Certificate IV in Business</h2>
    <p class="course-card__body">Lorem ipsum dolor sit amet, consectetur adipiscing elit. Pellentesque vitae eros at sem placerat hendrerit at a neque. Donec ac libero quis eros aliquet sollicitudin nec ac metus. Maecenas tellus tellus, tempor id bibendum ut, scelerisque lacinia justo. Suspendisse libero purus, egestas id vehicula at, lacinia sit amet turpis. Proin pellentesque libero ac leo vehicula bibendum. Vivamus placerat tincidunt vulputate. Phasellus luctus, eros ut porttitor sagittis, orci metus vehicula felis, at posuere lectus sem eu ante. Aliquam pellentesque quam ut sem aliquam nec consectetur nisl porttitor. Morbi suscipit gravida lorem quis blandit. Vivamus in imperdiet erat. Aenean id est eget neque mattis ornare. Fusce lacinia mauris vitae ante rutrum ultricies. Donec porta pharetra diam eu bibendum. Aliquam erat volutpat. Mauris quis urna lacus.</p>
    <p class="course-card__code">CRS40110 REG CODE: 100211A</p>
  </section>

  <section class="course-card col-left row-2">
    <h2 class="course-card__title">Diploma of Management</h2>
    <p class="course-card__body">Lorem ipsum dolor sit amet, consectetur adipiscing elit. Pellentesque vitae eros at sem placerat hendrerit at a neque. Donec ac libero quis eros aliquet sollicitudin nec ac metus. Maecenas tellus tellus, tempor id bibendum ut, scelerisque lacinia justo. Suspendisse libero purus, egestas id vehicula at, lacinia sit amet turpis. Proin pellentesque libero ac leo vehicula bibendum. Vivamus placerat tincidunt vulputate. Phasellus luctus, eros ut porttitor sagittis, orci metus vehicula felis, at posuere lectus sem eu ante. Aliquam pellentesque quam ut sem aliquam nec consectetur nisl porttitor. Morbi suscipit gravida lorem quis blandit. Vivamus in imperdiet erat. Aenean id est eget neque mattis ornare. Fusce lacinia mauris vitae ante rutrum ultricies. Donec porta pharetra diam eu bibendum. Aliquam erat volutpat. Mauris quis urna lacus.</p>
    <p class="course-card__code">CRS50120 REG CODE:100322B</p>
  </section>

  <section class="course-card col-left row-3">
    <h2 class="course-card__title">Advance Diploma of Management</h2>
    <p class="course-card__body">Lorem ipsum dolor sit amet, consectetur adipiscing elit. Pellentesque vitae eros at sem placerat hendrerit at a neque. Donec ac libero quis eros aliquet sollicitudin nec ac metus. Maecenas tellus tellus, tempor id bibendum ut, scelerisque lacinia justo. Suspendisse libero purus, egestas id vehicula at, lacinia sit amet turpis. Proin pellentesque libero ac leo vehicula bibendum. Vivamus placerat tincidunt vulputate. Phasellus luctus, eros ut porttitor sagittis, orci metus vehicula felis, at posuere lectus sem eu ante. Aliquam pellentesque quam ut sem aliquam nec consectetur nisl porttitor. Morbi suscipit gravida lorem quis blandit. Vivamus in imperdiet erat. Aenean id est eget neque mattis ornare. Fusce lacinia mauris vitae ante rutrum ultricies. Donec porta pharetra diam eu bibendum. Aliquam erat volutpat. Mauris quis urna lacus.</p>
    <p class="course-card__code">CRS60130 REG CODE: 100433C</p>
  </section>

  <section class="course-card course-card--sub col-left row-4">
    <h2 class="course-card__title">Certificate III in Hospitality</h2>
    <p class="course-card__subtitle">(Commercial Cookery)</p>
    <p class="course-card__body">Lorem ipsum dolor sit amet, consectetur adipiscing elit. Pellentesque vitae eros at sem placerat hendrerit at a neque. Donec ac libero quis eros aliquet sollicitudin nec ac metus. Maecenas tellus tellus, tempor id bibendum ut, scelerisque lacinia justo. Suspendisse libero purus, egestas id vehicula at, lacinia sit amet turpis. Proin pellentesque libero ac leo vehicula bibendum. Vivamus placerat tincidunt vulputate. Phasellus luctus, eros ut porttitor sagittis, orci metus vehicula felis, at posuere lectus sem eu ante. Aliquam pellentesque quam ut sem aliquam nec consectetur nisl porttitor. Morbi suscipit gravida lorem quis blandit. Vivamus in imperdiet erat. Aenean id est eget neque mattis ornare. Fusce lacinia mauris vitae ante rutrum ultricies. Donec porta pharetra diam eu bibendum. Aliquam erat volutpat. Mauris quis urna lacus.</p>
    <p class="course-card__code">HSP30140 REG CODE:100544D</p>
  </section>

  <section class="course-card col-right row-1">
    <h2 class="course-card__title">Certificate III in Hospitality(Patisserie)</h2>
    <p class="course-card__body">Lorem ipsum dolor sit amet, consectetur adipiscing elit. Pellentesque vitae eros at sem placerat hendrerit at a neque. Donec ac libero quis eros aliquet sollicitudin nec ac metus. Maecenas tellus tellus, tempor id bibendum ut, scelerisque lacinia justo. Suspendisse libero purus, egestas id vehicula at, lacinia sit amet turpis. Proin pellentesque libero ac leo vehicula bibendum. Vivamus placerat tincidunt vulputate. Phasellus luctus, eros ut porttitor sagittis, orci metus vehicula felis, at posuere lectus sem eu ante. Aliquam pellentesque quam ut sem aliquam nec consectetur nisl porttitor. Morbi suscipit gravida lorem quis blandit. Vivamus in imperdiet erat. Aenean id est eget neque mattis ornare. Fusce lacinia mauris vitae ante rutrum ultricies. Donec porta pharetra diam eu bibendum. Aliquam erat volutpat. Mauris quis urna lacus.</p>
    <p class="course-card__code">HSP31150 REG CODE:1006551E</p>
  </section>

  <section class="course-card course-card--sub col-right row-2">
    <h2 class="course-card__title">Certificate IV in Hospitality</h2>
    <p class="course-card__subtitle">(Commercial Cookery)</p>
    <p class="course-card__body">Lorem ipsum dolor sit amet, consectetur adipiscing elit. Pellentesque vitae eros at sem placerat hendrerit at a neque. Donec ac libero quis eros aliquet sollicitudin nec ac metus. Maecenas tellus tellus, tempor id bibendum ut, scelerisque lacinia justo. Suspendisse libero purus, egestas id vehicula at, lacinia sit amet turpis. Proin pellentesque libero ac leo vehicula bibendum. Vivamus placerat tincidunt vulputate. Phasellus luctus, eros ut porttitor sagittis, orci metus vehicula felis, at posuere lectus sem eu ante. Aliquam pellentesque quam ut sem aliquam nec consectetur nisl porttitor. Morbi suscipit gravida lorem quis blandit. Vivamus in imperdiet erat. Aenean id est eget neque mattis ornare. Fusce lacinia mauris vitae ante rutrum ultricies. Donec porta pharetra diam eu bibendum. Aliquam erat volutpat. Mauris quis urna lacus.</p>
    <p class="course-card__code">HSP40160 REG CODE:100766F</p>
  </section>

  <section class="course-card col-right row-3">
    <h2 class="course-card__title">Diploma of Hospitality</h2>
    <p class="course-card__body">Lorem ipsum dolor sit amet, consectetur adipiscing elit. Pellentesque vitae eros at sem placerat hendrerit at a neque. Donec ac libero quis eros aliquet sollicitudin nec ac metus. Maecenas tellus tellus, tempor id bibendum ut, scelerisque lacinia justo. Suspendisse libero purus, egestas id vehicula at, lacinia sit amet turpis. Proin pellentesque libero ac leo vehicula bibendum. Vivamus placerat tincidunt vulputate. Phasellus luctus, eros ut porttitor sagittis, orci metus vehicula felis, at posuere lectus sem eu ante. Aliquam pellentesque quam ut sem aliquam nec consectetur nisl porttitor. Morbi suscipit gravida lorem quis blandit. Vivamus in imperdiet erat. Aenean id est eget neque mattis ornare. Fusce lacinia mauris vitae ante rutrum ultricies. Donec porta pharetra diam eu bibendum. Aliquam erat volutpat. Mauris quis urna lacus.</p>
    <p class="course-card__code">HSP50170 REG CODE:100877G</p>
  </section>

  <div class="student-photo" role="img" aria-label="Photo of a group of smiling students sitting together outdoors under palm trees"></div>

  <div class="band band--bottom"></div>
</main>
</body>
</html>
```